One of a Kind Clean Business Card

We need to design a new business card template for our company. Our company designs and produced merchandising displays. You can see a sample of what we produce on our site www.qorvatfixtures.com. I have uploaded our logo in vector format, as well as a picture of our current business cards. We want a totally different look. We want simple and clean, looking forward to seeing what people create.
Updates

I would like to update the address for Tellur Display Group Inc. 418 N Brindle Ave Arlington Heights, IL 60817 Would also note. No QR codes

Industry/Entity Type

Business

Contact Information for Business Card

Need a 1 sided business card designed.

Font styles to use
Serif

Requirements
Must have
• Easy to view; Clean Design
Nice to have
• Features that promote engineering and creativity
Should not have
• Too much clutter, keep it simple

```html
<!DOCTYPE html>
<html lang="en">
<head>
<meta charset="utf-8">
<title>Tellur Display Group Inc. — Business Card</title>
<link rel="stylesheet" href="https://fonts.googleapis.com/css2?family=Open+Sans:wght@400;600&display=swap">
<style>
  :root {
    --backdrop: #1e1e1f;
    --card: #fdfdfa;
    --ink: #1a1a1a;
    --surname: #6b3a12;
    --brand-red: #9b1c24;
    --band-tan: #d9a48f;
    --band-text: #ffffff;
  }
  * { margin: 0; padding: 0; box-sizing: border-box; }
  html, body {
    width: 1200px; height: 837px; overflow: hidden;
    background: var(--backdrop);
    font-family: "Open Sans", sans-serif;
  }
  .canvas {
    position: relative; width: 1200px; height: 837px;
    display: flex; align-items: center; justify-content: center;
  }
  .business-card {
    position: relative; width: 900px; height: 514px;
    background: var(--card); border-radius: 34px; overflow: hidden;
  }
  .company-name {
    position: absolute; left: 60px; top: 56px;
    font-size: 44px; font-weight: 400; color: var(--brand-red);
    letter-spacing: 0.5px;
  }
  .person-name {
    position: absolute; left: 60px; top: 196px;
    font-size: 40px; font-weight: 400; color: var(--ink);
  }
  .person-name .surname { color: var(--surname); }
  .contact {
    position: absolute; top: 268px;
    font-size: 21px; color: var(--ink); line-height: 34px; list-style: none;
  }
  .contact-phones { left: 60px; }
  .contact-reach { left: 300px; top: 302px; }
  .contact .label { font-weight: 600; margin-right: 6px; }
  .footer-band {
    position: absolute; left: 0; right: 0; bottom: 0; height: 86px;
    background: var(--brand-red);
    border-top: 12px solid var(--band-tan);
    display: flex; align-items: center; padding-left: 60px;
  }
  .website {
    color: var(--band-text); font-size: 24px; font-weight: 600;
    letter-spacing: 3px;
  }
</style>
</head>
<body>
<main class="canvas">
  <article class="business-card">
    <h1 class="company-name">Tellur Display Group Inc.</h1>
    <h2 class="person-name">Walt <span class="surname">Renner</span></h2>
    <ul class="contact contact-phones">
      <li><span class="label">O:</span>815-555-0142</li>
      <li><span class="label">C:</span>312-555-0176</li>
    </ul>
    <ul class="contact contact-reach">
      <li><span class="label">E:</span>wrenner@qorvatfixtures.com</li>
      <li><span class="label">L:</span>418 N Brindle Ave Arlington Heights, IL 60817</li>
    </ul>
    <footer class="footer-band">
      <span class="website">www.qorvatfixtures.com</span>
    </footer>
  </article>
</main>
</body>
</html>
```